WILLOWMERE PERK WEBSITE HOME PAGE AND CHECKOUT PAGES

UPDATE TO BRIEF:

Willowmere Perks is a company that provides Charities with the Free Vacation Vouchers that they can use to incentivize people to donate which in turn increases donations for the chairty.

So I need to keep it a little more template like the example url I gave. http://plinthframes.com/willowmere-perk/ Because, I am going to provide template to ANY CHARITY TYPE and they just fill in the content into the template and change images or whatever for their charity. So I am really looking for a website template that can be used for multiple and different kinds of charities.

So where the logo would go please use YOUR LOGO HERE generic logo for now

and where ever you promote the Free Vacation Certificate To Las Vegas please add "Brought To You By" (logo willowmere perks or something...basically its a partnership with the Charity and Willowmere Perk)

So Willowmere Perk is a marketing company and not a Charity but more of a plug and play platform that allows a charity to accepts donations and immediately deliver the promised incentive offer after donation is made on the website.

When a Charity is able to offer a high perceived value gift for a donation they increase donations.

Target Market(s)

PEOPLE THAT DONATE TO CHARITIES

Industry/Entity Type

Charity

Number of Pages Required

3 page

Requirements
Must have
• One thing i need to add to the website is an Incentive Gift for the Donation.

So I need this tagline and images to make the promotion seem great:
"Donate $100 and Receive A Free 3 Night Vacation Certificate To Las Vegas!"

Maybe show image of vegas or some kind of nice graphic that promotes the vegas vacation as a gift for the $100 donation very well"

I need the payment pages as well. So when someone click Donate Now, the next page is there where they can see their gift that is included with the donation, and also the donation amount...
Nice to have

Should not have

```html
<!DOCTYPE html>
<html lang="en">
<head>
<meta charset="utf-8">
<title>Willowmere Perk – Charity Donation Template</title>
<link rel="stylesheet" href="https://fonts.googleapis.com/css2?family=Jost:wght@400;500;600;700&display=swap">
<style>
  :root {
    --stage: #06b5de;
    --cyan: #1cb6e0;
    --cyan-deep: #129fc8;
    --orange: #f07c12;
    --ink: #3b3b3b;
    --ink-soft: #5d5d5d;
    --muted: #8b8b8b;
    --pill: #e6e7e9;
    --band: #e9ebee;
    --dark-btn: #4b4b4b;
    --white: #ffffff;
    --line: #ececec;
    --scrim: rgba(120, 120, 120, 0.42);
  }
  * { box-sizing: border-box; margin: 0; padding: 0; }
  html, body { width: 1200px; height: 2366px; overflow: hidden; }
  body {
    background: var(--stage);
    font-family: "Jost", "Futura", sans-serif;
    color: var(--ink);
    position: relative;
  }
  .panel {
    position: absolute; top: 23px; width: 515px; height: 2318px;
    background: var(--white); overflow: hidden;
    box-shadow: 0 4px 14px rgba(0,0,0,0.18);
  }
  .panel--page { left: 52px; }
  .panel--checkout { left: 632px; }
  .panel > * { position: absolute; }

  /* header */
  .site-header { left: 0; top: 0; width: 515px; height: 38px; background: var(--white); }
  .site-logo { position: absolute; left: 38px; top: 11px; font-size: 12px; font-weight: 700; color: var(--cyan); letter-spacing: 0.3px; }
  .btn {
    position: absolute; display: flex; align-items: center; justify-content: center;
    font-size: 6.5px; font-weight: 700; color: var(--white); background: var(--cyan);
    border-radius: 2px; letter-spacing: 0.3px; text-transform: uppercase;
    box-shadow: 0 1px 2px rgba(0,0,0,0.15);
  }
  .btn--dark { background: var(--dark-btn); }
  .btn--donor { left: 400px; top: 10px; width: 77px; height: 18px; }

  /* hero */
  .hero {
    left: 0; top: 38px; width: 515px; height: 252px;
    background:
      radial-gradient(ellipse 120px 90px at 140px 200px, rgba(190,120,255,0.55), transparent 70%),
      radial-gradient(ellipse 160px 70px at 360px 220px, rgba(255,150,60,0.45), transparent 70%),
      radial-gradient(ellipse 90px 120px at 390px 120px, rgba(255,190,90,0.35), transparent 70%),
      linear-gradient(180deg, #0e1030 0%, #1c1840 40%, #3a2a5c 70%, #5a3e5e 100%);
  }
  .hero-title { position: absolute; left: 38px; top: 66px; font-size: 26px; font-weight: 700; color: var(--white); letter-spacing: 0.5px; }
  .hero-sub { position: absolute; left: 38px; top: 94px; width: 260px; font-size: 14px; line-height: 19px; color: var(--white); font-weight: 400; }
  .btn--hero { left: 38px; top: 137px; width: 67px; height: 17px; }

  /* summary */
  .summary-photo {
    left: 38px; top: 313px; width: 192px; height: 139px; border-radius: 3px;
    background:
      radial-gradient(ellipse 70px 40px at 120px 80px, rgba(255,170,80,0.6), transparent 70%),
      linear-gradient(180deg, #13315f 0%, #1d3f73 45%, #3b3f62 75%, #1a1f33 100%);
    box-shadow: 0 1px 3px rgba(0,0,0,0.3);
  }
  .summary-photo-caption { position: absolute; left: 0; bottom: 8px; width: 100%; text-align: center; font-size: 6px; font-weight: 700; color: var(--white); }
  .brought-by { display: flex; align-items: center; gap: 8px; }
  .brought-by--summary { left: 42px; top: 466px; }
  .brought-label { font-size: 5px; font-weight: 700; color: var(--ink); }
  .partner-mark { display: flex; align-items: center; gap: 5px; }
  .partner-dot { width: 14px; height: 14px; border-radius: 50%; background: var(--cyan); }
  .partner-name { font-size: 12px; font-weight: 600; color: var(--cyan-deep); line-height: 1; }
  .summary-divider { left: 258px; top: 290px; width: 1px; height: 218px; background: var(--line); }
  .summary-pitch { left: 304px; top: 312px; width: 180px; font-size: 7.5px; line-height: 11px; color: var(--ink-soft); }
  .btn--donate-now { left: 348px; top: 344px; width: 77px; height: 17px; }
  .btn--share { left: 348px; top: 367px; width: 77px; height: 17px; }
  .stat-big { font-size: 20px; font-weight: 700; color: var(--ink-soft); line-height: 1; }
  .stat-donors { left: 304px; top: 396px; }
  .stat-raised { left: 304px; top: 431px; }
  .stat-label { font-size: 7px; font-weight: 700; color: var(--cyan); }
  .stat-donors-label { left: 304px; top: 418px; }
  .stat-raised-label { left: 304px; top: 453px; }
  .progress { left: 304px; top: 473px; width: 166px; height: 4px; border-radius: 2px; background: #e1e1e1; }
  .progress-fill { position: absolute; left: 0; top: 0; width: 54px; height: 4px; border-radius: 2px; background: var(--cyan); }
  .progress-meta { left: 304px; top: 482px; width: 166px; display: flex; justify-content: space-between; font-size: 4.5px; font-weight: 700; color: var(--ink-soft); }
  .progress-meta span b { color: var(--cyan); }

  /* story sections */
  .section-rule { left: 0; width: 515px; height: 1px; background: var(--line); }
  .tag { font-size: 8px; color: var(--ink-soft); background: var(--pill); padding: 2px 5px; letter-spacing: 0.2px; }
  .section-heading { font-size: 8px; font-weight: 700; color: var(--cyan); letter-spacing: 0.2px; }
  .section-heading--warm { color: var(--orange); }
  .body-copy { font-size: 7.6px; line-height: 11.3px; color: var(--ink-soft); }
  .body-copy p + p { margin-top: 11.3px; }
  .photo { border-radius: 2px; box-shadow: 0 1px 3px rgba(0,0,0,0.25); }
  .photo--panda-rock { background: linear-gradient(160deg, #6c6a63 0%, #3e3d39 45%, #8c8a84 75%, #54524c 100%); }
  .photo--panda-bamboo { background: linear-gradient(160deg, #7b8a5d 0%, #5b6544 40%, #8b8170 75%, #6e6654 100%); }
  .photo--panda-mono { background: linear-gradient(160deg, #9a9a9a 0%, #5e5e5e 50%, #b3b3b3 100%); }
  .photo--panda-tree { background: linear-gradient(160deg, #556b3a 0%, #3a4e28 45%, #6f7b4d 75%, #45552e 100%); }
  .photo--panda-cub { background: linear-gradient(160deg, #6f8a4a 0%, #4d5f35 50%, #8a9070 100%); }

  .facts-tag { left: 38px; top: 541px; }
  .facts-heading { left: 38px; top: 563px; }
  .facts-copy { left: 38px; top: 581px; width: 170px; }
  .facts-photo { left: 273px; top: 547px; width: 205px; height: 175px; }
  .conservation { left: 273px; top: 731px; width: 205px; text-align: center; }
  .conservation-title { font-size: 7.5px; color: var(--ink-soft); letter-spacing: 0.2px; }
  .conservation-value { font-size: 7.5px; color: var(--cyan); margin-top: 3px; }
  .fact-cell { width: 62px; text-align: center; }
  .fact-label { font-size: 5px; font-weight: 700; color: var(--ink-soft); background: var(--pill); height: 11px; line-height: 11px; border-radius: 1px; }
  .fact-value { font-size: 5.5px; font-weight: 700; color: var(--ink); margin-top: 3px; }
  .fact--pop { left: 296px; top: 759px; }
  .fact--life { left: 392px; top: 759px; }
  .fact--weight { left: 296px; top: 791px; }
  .fact--sci { left: 392px; top: 791px; }

  .issues-photo { left: 38px; top: 861px; width: 205px; height: 175px; }
  .issues-tag { left: 315px; top: 846px; }
  .issues-heading { left: 315px; top: 868px; }
  .issues-copy { left: 315px; top: 886px; width: 165px; }

  .urgency-tag { left: 38px; top: 1090px; }
  .urgency-heading { left: 38px; top: 1112px; }
  .urgency-copy { left: 38px; top: 1130px; width: 170px; }
  .urgency-photo { left: 273px; top: 1103px; width: 205px; height: 175px; }

  /* testimonial */
  .testimonial { left: 0; top: 1308px; width: 515px; height: 122px; background: var(--band); }
  .testimonial-quote { position: absolute; left: 71px; top: 13px; width: 373px; text-align: center; font-size: 6px; line-height: 8.8px; font-weight: 700; color: var(--ink); }
  .testimonial-name { position: absolute; left: 0; top: 43px; width: 515px; text-align: center; font-size: 7px; color: var(--orange); }
  .testimonial-role { position: absolute; left: 0; top: 53px; width: 515px; text-align: center; font-size: 5.5px; color: var(--ink-soft); }
  .testimonial-avatar { position: absolute; left: 247px; top: 65px; width: 20px; height: 20px; border-radius: 50%; background: linear-gradient(160deg, #d9a27f, #b9703f); border: 1px solid var(--white); }
  .testimonial-arrow { position: absolute; top: 51px; font-size: 13px; color: var(--ink-soft); }
  .testimonial-arrow--prev { left: 48px; }
  .testimonial-arrow--next { left: 458px; }
  .btn--testimonial { left: 219px; top: 93px; width: 77px; height: 17px; }
  .testimonial-pointer { left: 248px; top: 1430px; width: 0; height: 0; border-left: 9px solid transparent; border-right: 9px solid transparent; border-top: 12px solid var(--band); }

  /* solution */
  .solution-tag { left: 84px; top: 1454px; }
  .solution-heading { left: 84px; top: 1476px; }
  .solution-copy { left: 84px; top: 1494px; width: 355px; }
  .solution-video { left: 86px; top: 1544px; width: 366px; height: 204px; background: linear-gradient(160deg, #4d6536 0%, #35482a 40%, #5f6f40 70%, #2e3c22 100%); }
  .play-button { position: absolute; left: 156px; top: 75px; width: 54px; height: 54px; }

  .feature-photo { width: 119px; height: 101px; }
  .feature-heading { }
  .feature-copy { width: 215px; }
  .feature-1-photo { left: 86px; top: 1779px; }
  .feature-1-heading { left: 224px; top: 1786px; }
  .feature-1-copy { left: 224px; top: 1803px; }
  .feature-2-heading { left: 86px; top: 1914px; }
  .feature-2-copy { left: 86px; top: 1931px; }
  .feature-2-photo { left: 333px; top: 1907px; }
  .feature-3-photo { left: 86px: top: 2035px; }
  .feature-3-photo { left: 86px; top: 2035px; }
  .feature-3-heading { left: 224px; top: 2042px; }
  .feature-3-copy { left: 224px; top: 2059px; }

  /* footer */
  .closing-band { left: 0; top: 2197px; width: 515px; height: 121px; background: linear-gradient(180deg, #2ac0e3 0%, #1bb1da 100%); }
  .closing-line { position: absolute; left: 0; top: 29px; width: 515px; text-align: center; font-size: 15px; line-height: 21px; font-weight: 700; color: var(--white); }
  .btn--closing { left: 219px; top: 75px; width: 77px; height: 17px; }

  /* checkout overlay */
  .scrim { left: 0; top: 0; width: 515px; height: 2318px; background: var(--scrim); }
  .checkout-modal { left: 117px; top: 264px; width: 282px; height: 386px; background: var(--white); box-shadow: 0 2px 10px rgba(0,0,0,0.25); }
  .checkout-modal > * { position: absolute; }
  .modal-header { left: 0; top: 0; width: 282px; height: 28px; border-bottom: 1px solid var(--line); }
  .modal-title { position: absolute; left: 33px; top: 8px; font-size: 8px; font-weight: 600; color: var(--ink); }
  .modal-close { position: absolute; right: 30px; top: 9px; width: 9px; height: 9px; }
  .modal-label { font-size: 5.5px; color: var(--ink-soft); }
  .amount-label { left: 33px; top: 46px; }
  .amount-box { left: 33px; top: 58px; width: 88px; height: 28px; border: 1px solid #dcdcdc; display: flex; align-items: center; }
  .amount-currency { width: 18px; height: 100%; display: flex; align-items: center; justify-content: center; font-size: 17px; font-weight: 700; color: var(--ink); border-right: 1px solid #dcdcdc; }
  .amount-value { padding-left: 6px; font-size: 15px; font-weight: 600; color: var(--ink); }
  .amount-note { left: 33px; top: 93px; }
  .donating-label { left: 33px; top: 119px; }
  .charity-logo { left: 33px; top: 132px; width: 60px; text-align: center; font-size: 16px; line-height: 20px; font-weight: 700; color: var(--cyan); }
  .monthly { left: 33px; top: 178px; display: flex; align-items: center; gap: 4px; }
  .check-box { width: 7px; height: 7px; border: 1px solid #cfcfcf; background: var(--white); }
  .details-label { left: 145px; top: 46px; }
  .field { height: 14px; border: 1px solid #d8d8d8; font-size: 4.5px; color: var(--muted); padding-left: 5px; display: flex; align-items: center; }
  .field--name { left: 145px; top: 58px; width: 104px; }
  .field-social { position: absolute; right: 2px; top: 2px; width: 8px; height: 8px; background: #3b5c9b; }
  .field--email { left: 145px; top: 78px; width: 104px; }
  .field--billing { left: 145px; top: 97px; width: 104px; }
  .field--zip { left: 145px; top: 116px; width: 38px; }
  .field--card { left: 145px; top: 136px; width: 104px; }
  .field--month { left: 145px; top: 155px; width: 30px; }
  .field--year { left: 183px; top: 155px; width: 30px; }
  .field--cvv { left: 220px; top: 155px; width: 29px; }
  .field--message { left: 145px; top: 174px; width: 104px; height: 37px; align-items: flex-start; padding-top: 4px; }
  .modal-rule { left: 0; top: 224px; width: 282px; height: 1px; background: var(--line); }
  .robot-check { left: 33px; top: 234px; width: 110px; height: 29px; border: 1px solid #d3d3d3; background: #f9f9f9; border-radius: 2px; }
  .robot-check .check-box { position: absolute; left: 7px; top: 10px; width: 9px; height: 9px; }
  .robot-text { position: absolute; left: 20px; top: 11px; font-size: 4.5px; color: var(--ink); }
  .robot-badge { position: absolute; right: 8px; top: 6px; width: 10px; height: 10px; border-radius: 50%; background: #9aa7c4; }
  .robot-legal { position: absolute; right: 4px; top: 19px; font-size: 3px; color: var(--muted); }
  .btn--submit { left: 154px; top: 240px; width: 90px; height: 19px; font-size: 6px; }
  .included-copy { left: 28px; top: 284px; width: 116px; text-align: center; font-size: 11.5px; line-height: 15.2px; font-weight: 700; color: var(--ink); }
  .certificate-card { left: 151px; top: 280px; width: 98px; height: 66px; border-radius: 5px; background: linear-gradient(160deg, #163a6f 0%, #24487d 50%, #4a3d61 100%); box-shadow: 0 1px 3px rgba(0,0,0,0.3); }
  .brought-by--modal { left: 151px; top: 349px; display: block; }
  .brought-by--modal .brought-label { font-size: 3.5px; }
  .brought-by--modal .partner-mark { margin-top: 4px; }
  .brought-by--modal .partner-dot { width: 11px; height: 11px; }
  .brought-by--modal .partner-name { font-size: 9.5px; }
</style>
</head>
<body>

<!-- Landing page -->
<main class="panel panel--page">
  <header class="site-header">
    <div class="site-logo">LOGO HERE</div>
    <div class="btn btn--donor">Become a Donor</div>
  </header>

  <section class="hero" role="img" aria-label="Night skyline of the Las Vegas Strip with fountains and lights">
    <h1 class="hero-title">DONATE $100</h1>
    <p class="hero-sub">GET A FREE 3 NIGHTS VACATION CERTIFICATE FOR LAS VEGAS!</p>
    <div class="btn btn--hero">Donate Today</div>
  </section>

  <div class="summary-photo" role="img" aria-label="Las Vegas at dusk, vacation certificate promotion">
    <span class="summary-photo-caption">3 NIGHTS VACATION CERTIFICATE FOR LAS VEGAS!</span>
  </div>
  <div class="brought-by brought-by--summary">
    <span class="brought-label">Brought To You By:</span>
    <span class="partner-mark"><span class="partner-dot"></span><span class="partner-name">Willowmere Perks</span></span>
  </div>
  <div class="summary-divider"></div>
  <p class="summary-pitch">Donate today &amp; help us reach our $1M goal to Lorem ipsum dolor sit amet, consectetur adipisici</p>
  <div class="btn btn--donate-now">Donate Now</div>
  <div class="btn btn--dark btn--share">Share</div>
  <div class="stat-big stat-donors">350</div>
  <div class="stat-label stat-donors-label">DONORS</div>
  <div class="stat-big stat-raised">$200,728</div>
  <div class="stat-label stat-raised-label">RAISED (USD)</div>
  <div class="progress"><div class="progress-fill"></div></div>
  <div class="progress-meta"><span>Goal: <b>$1 000 000</b></span><span>Days Left: <b>26</b></span></div>

  <div class="section-rule" style="top:508px"></div>
  <span class="tag facts-tag">THE FACTS</span>
  <h2 class="section-heading facts-heading">PERSPICIATIS UNDE OMNIS</h2>
  <div class="body-copy facts-copy">
    <p>Lorem ipsum dolor sit amet, consectetur adipiscing elit, sed do eiusmod tempor incididunt ut labore et dolore magna aliqua. Ut enim ad minim veniam. Duis aute irure dolor in reprehenderit in voluptate velit esse cillum dolore eu fugiat nulla pariatur. Excepteur sint occaecat cupidatat non proident.</p>
    <p>Lorem ipsum dolor sit amet, consectetur adipiscing elit, sed do eiusmod tempor incididunt ut labore et dolore magna aliqua. Ut enim ad minim veniam, quis nostrud exercitation ullamco laboris nisi ut aliquip ex ea commodo consequat.</p>
  </div>
  <div class="photo photo--panda-rock facts-photo" role="img" aria-label="Giant panda sitting on rocks"></div>
  <div class="conservation">
    <div class="conservation-title">CONSERVATION STATUS</div>
    <div class="conservation-value">Vulnerable</div>
  </div>
  <div class="fact-cell fact--pop"><div class="fact-label">EST POPULATION</div><div class="fact-value">10,000-15,000</div></div>
  <div class="fact-cell fact--life"><div class="fact-label">LIFESPAN</div><div class="fact-value">30-50 years</div></div>
  <div class="fact-cell fact--weight"><div class="fact-label">WEIGHT</div><div class="fact-value">210-520kg</div></div>
  <div class="fact-cell fact--sci"><div class="fact-label">SCIENTIFIC NAME</div><div class="fact-value">Ailuropoda melanoleuca</div></div>

  <div class="section-rule" style="top:828px"></div>
  <div class="photo photo--panda-bamboo issues-photo" role="img" aria-label="Panda eating bamboo"></div>
  <span class="tag issues-tag">THE ISSUES</span>
  <h2 class="section-heading section-heading--warm issues-heading">PERSPICIATIS UNDE OMNIS</h2>
  <div class="body-copy issues-copy">
    <p>Lorem ipsum dolor sit amet, consectetur adipiscing elit, sed do eiusmod tempor incididunt ut labore et dolore magna aliqua. Ut enim ad minim veniam. Duis aute irure dolor in reprehenderit in voluptate velit esse cillum dolore eu fugiat nulla pariatur. Excepteur sint occaecat cupidatat non proident.</p>
    <p>Lorem ipsum dolor sit amet, consectetur adipiscing elit, sed do eiusmod tempor incididunt ut labore et dolore magna aliqua. Ut enim ad minim veniam, quis nostrud exercitation ullamco laboris nisi ut aliquip ex ea commodo consequat.</p>
  </div>

  <div class="section-rule" style="top:1064px"></div>
  <span class="tag urgency-tag">THE URGENCY</span>
  <h2 class="section-heading urgency-heading">PERSPICIATIS UNDE OMNIS</h2>
  <div class="body-copy urgency-copy">
    <p>Lorem ipsum dolor sit amet, consectetur adipiscing elit, sed do eiusmod tempor incididunt ut labore et dolore magna aliqua. Ut enim ad minim veniam. Duis aute irure dolor in reprehenderit in voluptate velit esse cillum dolore eu fugiat nulla pariatur. Excepteur sint occaecat cupidatat non proident.</p>
    <p>Lorem ipsum dolor sit amet, consectetur adipiscing elit, sed do eiusmod tempor incididunt ut labore et dolore magna aliqua. Ut enim ad minim veniam, quis nostrud exercitation ullamco laboris nisi ut aliquip ex ea commodo consequat.</p>
  </div>
  <div class="photo photo--panda-mono urgency-photo" role="img" aria-label="Black and white photo of a panda eating"></div>

  <section class="testimonial">
    <p class="testimonial-quote">"Lorem ipsum dolor sit amet, consectetur adipisicing elit, sed do eiusmod tempor incididunt ut labore et dolore magna aliqua. Ut enim ad minim veniam. Duis aute irure dolor in reprehenderit in voluptate velit esse cillum dolore eu fugiat nulla pariatur. Excepteur sint occaecat cupidatat non proident."</p>
    <span class="testimonial-arrow testimonial-arrow--prev">&laquo;</span>
    <span class="testimonial-arrow testimonial-arrow--next">&raquo;</span>
    <div class="testimonial-name">Helena Varga</div>
    <div class="testimonial-role">CO-FOUNDER OF BAMBOO HAVEN</div>
    <div class="testimonial-avatar" role="img" aria-label="Portrait of the co-founder"></div>
    <div class="btn btn--testimonial">Donate Now</div>
  </section>
  <div class="testimonial-pointer"></div>

  <span class="tag solution-tag">THE SOLUTION</span>
  <h2 class="section-heading solution-heading">PERSPICIATIS UNDE OMNIS</h2>
  <p class="body-copy solution-copy">Lorem ipsum dolor sit amet, consectetur adipiscing elit, sed do eiusmod tempor incididunt ut labore et dolore magna aliqua. Ut enim ad minim veniam. Duis aute irure dolor in reprehenderit in voluptate velit esse cillum dolore eu fugiat nulla pariatur. Excepteur sint occaecat cupidatat non proident.</p>
  <div class="solution-video" role="img" aria-label="Video still of a panda climbing a tree">
    <svg class="play-button" viewBox="0 0 54 54"><circle cx="27" cy="27" r="25" fill="rgba(0,0,0,0.15)" stroke="#fff" stroke-width="1.5"/><path d="M22 18 L36 27 L22 36 Z" fill="#fff"/></svg>
  </div>

  <div class="photo photo--panda-cub feature-photo feature-1-photo" role="img" aria-label="Panda cub resting on a branch"></div>
  <h3 class="section-heading section-heading--warm feature-1-heading">PERSPICIATIS UNDE OMNIS</h3>
  <p class="body-copy feature-copy feature-1-copy">Lorem ipsum dolor sit amet, consectetur adipiscing elit, sed do eiusmod tempor incididunt ut labore et dolore magna aliqua. Ut enim ad minim veniam. Duis aute irure dolor in reprehenderit in voluptate velit esse cillum dolore eu fugiat nulla pariatur. Excepteur sint occaecat cupidatat non proident.</p>

  <h3 class="section-heading feature-2-heading">PERSPICIATIS UNDE OMNIS</h3>
  <p class="body-copy feature-copy feature-2-copy">Lorem ipsum dolor sit amet, consectetur adipiscing elit, sed do eiusmod tempor incididunt ut labore et dolore magna aliqua. Ut enim ad minim veniam. Duis aute irure dolor in reprehenderit in voluptate velit esse cillum dolore eu fugiat nulla pariatur. Excepteur sint occaecat cupidatat non proident.</p>
  <div class="photo photo--panda-bamboo feature-photo feature-2-photo" role="img" aria-label="Panda eating bamboo"></div>

  <div class="photo photo--panda-tree feature-photo feature-3-photo" role="img" aria-label="Panda among bamboo stalks"></div>
  <h3 class="section-heading section-heading--warm feature-3-heading">PERSPICIATIS UNDE OMNIS</h3>
  <p class="body-copy feature-copy feature-3-copy">Lorem ipsum dolor sit amet, consectetur adipiscing elit, sed do eiusmod tempor incididunt ut labore et dolore magna aliqua. Ut enim ad minim veniam. Duis aute irure dolor in reprehenderit in voluptate velit esse cillum dolore eu fugiat nulla pariatur. Excepteur sint occaecat cupidatat non proident.</p>

  <section class="closing-band">
    <p class="closing-line">Donate today &amp; help us reach our $1M goal to<br>Lorem Ipsum is simply dummy text of the</p>
    <div class="btn btn--dark btn--closing">Donate Now</div>
  </section>
</main>

<!-- Checkout state -->
<main class="panel panel--checkout">
  <header class="site-header">
    <div class="site-logo">LOGO HERE</div>
    <div class="btn btn--donor">Become a Donor</div>
  </header>

  <section class="hero" role="img" aria-label="Night skyline of the Las Vegas Strip with fountains and lights">
    <h1 class="hero-title">DONATE $100</h1>
    <p class="hero-sub">GET A FREE 3 NIGHTS VACATION CERTIFICATE FOR LAS VEGAS!</p>
    <div class="btn btn--hero">Donate Today</div>
  </section>

  <div class="summary-photo" role="img" aria-label="Las Vegas at dusk, vacation certificate promotion">
    <span class="summary-photo-caption">3 NIGHTS VACATION CERTIFICATE FOR LAS VEGAS!</span>
  </div>
  <div class="brought-by brought-by--summary">
    <span class="brought-label">Brought To You By:</span>
    <span class="partner-mark"><span class="partner-dot"></span><span class="partner-name">Willowmere Perks</span></span>
  </div>
  <div class="summary-divider"></div>
  <p class="summary-pitch">Donate today &amp; help us reach our $1M goal to Lorem ipsum dolor sit amet, consectetur adipisici</p>
  <div class="btn btn--donate-now">Donate Now</div>
  <div class="btn btn--dark btn--share">Share</div>
  <div class="stat-big stat-donors">350</div>
  <div class="stat-label stat-donors-label">DONORS</div>
  <div class="stat-big stat-raised">$200,728</div>
  <div class="stat-label stat-raised-label">RAISED (USD)</div>
  <div class="progress"><div class="progress-fill"></div></div>
  <div class="progress-meta"><span>Goal: <b>$1 000 000</b></span><span>Days Left: <b>26</b></span></div>

  <div class="section-rule" style="top:508px"></div>
  <span class="tag facts-tag">THE FACTS</span>
  <h2 class="section-heading facts-heading">PERSPICIATIS UNDE OMNIS</h2>
  <div class="body-copy facts-copy">
    <p>Lorem ipsum dolor sit amet, consectetur adipiscing elit, sed do eiusmod tempor incididunt ut labore et dolore magna aliqua. Ut enim ad minim veniam. Duis aute irure dolor in reprehenderit in voluptate velit esse cillum dolore eu fugiat nulla pariatur. Excepteur sint occaecat cupidatat non proident.</p>
    <p>Lorem ipsum dolor sit amet, consectetur adipiscing elit, sed do eiusmod tempor incididunt ut labore et dolore magna aliqua. Ut enim ad minim veniam, quis nostrud exercitation ullamco laboris nisi ut aliquip ex ea commodo consequat.</p>
  </div>
  <div class="photo photo--panda-rock facts-photo" role="img" aria-label="Giant panda sitting on rocks"></div>
  <div class="conservation">
    <div class="conservation-title">CONSERVATION STATUS</div>
    <div class="conservation-value">Vulnerable</div>
  </div>
  <div class="fact-cell fact--pop"><div class="fact-label">EST POPULATION</div><div class="fact-value">10,000-15,000</div></div>
  <div class="fact-cell fact--life"><div class="fact-label">LIFESPAN</div><div class="fact-value">30-50 years</div></div>
  <div class="fact-cell fact--weight"><div class="fact-label">WEIGHT</div><div class="fact-value">210-520kg</div></div>
  <div class="fact-cell fact--sci"><div class="fact-label">SCIENTIFIC NAME</div><div class="fact-value">Ailuropoda melanoleuca</div></div>

  <div class="section-rule" style="top:828px"></div>
  <div class="photo photo--panda-bamboo issues-photo" role="img" aria-label="Panda eating bamboo"></div>
  <span class="tag issues-tag">THE ISSUES</span>
  <h2 class="section-heading section-heading--warm issues-heading">PERSPICIATIS UNDE OMNIS</h2>
  <div class="body-copy issues-copy">
    <p>Lorem ipsum dolor sit amet, consectetur adipiscing elit, sed do eiusmod tempor incididunt ut labore et dolore magna aliqua. Ut enim ad minim veniam. Duis aute irure dolor in reprehenderit in voluptate velit esse cillum dolore eu fugiat nulla pariatur. Excepteur sint occaecat cupidatat non proident.</p>
    <p>Lorem ipsum dolor sit amet, consectetur adipiscing elit, sed do eiusmod tempor incididunt ut labore et dolore magna aliqua. Ut enim ad minim veniam, quis nostrud exercitation ullamco laboris nisi ut aliquip ex ea commodo consequat.</p>
  </div>

  <div class="section-rule" style="top:1064px"></div>
  <span class="tag urgency-tag">THE URGENCY</span>
  <h2 class="section-heading urgency-heading">PERSPICIATIS UNDE OMNIS</h2>
  <div class="body-copy urgency-copy">
    <p>Lorem ipsum dolor sit amet, consectetur adipiscing elit, sed do eiusmod tempor incididunt ut labore et dolore magna aliqua. Ut enim ad minim veniam. Duis aute irure dolor in reprehenderit in voluptate velit esse cillum dolore eu fugiat nulla pariatur. Excepteur sint occaecat cupidatat non proident.</p>
    <p>Lorem ipsum dolor sit amet, consectetur adipiscing elit, sed do eiusmod tempor incididunt ut labore et dolore magna aliqua. Ut enim ad minim veniam, quis nostrud exercitation ullamco laboris nisi ut aliquip ex ea commodo consequat.</p>
  </div>
  <div class="photo photo--panda-mono urgency-photo" role="img" aria-label="Black and white photo of a panda eating"></div>

  <section class="testimonial">
    <p class="testimonial-quote">"Lorem ipsum dolor sit amet, consectetur adipisicing elit, sed do eiusmod tempor incididunt ut labore et dolore magna aliqua. Ut enim ad minim veniam. Duis aute irure dolor in reprehenderit in voluptate velit esse cillum dolore eu fugiat nulla pariatur. Excepteur sint occaecat cupidatat non proident."</p>
    <span class="testimonial-arrow testimonial-arrow--prev">&laquo;</span>
    <span class="testimonial-arrow testimonial-arrow--next">&raquo;</span>
    <div class="testimonial-name">Helena Varga</div>
    <div class="testimonial-role">CO-FOUNDER OF BAMBOO HAVEN</div>
    <div class="testimonial-avatar" role="img" aria-label="Portrait of the co-founder"></div>
    <div class="btn btn--testimonial">Donate Now</div>
  </section>
  <div class="testimonial-pointer"></div>

  <span class="tag solution-tag">THE SOLUTION</span>
  <h2 class="section-heading solution-heading">PERSPICIATIS UNDE OMNIS</h2>
  <p class="body-copy solution-copy">Lorem ipsum dolor sit amet, consectetur adipiscing elit, sed do eiusmod tempor incididunt ut labore et dolore magna aliqua. Ut enim ad minim veniam. Duis aute irure dolor in reprehenderit in voluptate velit esse cillum dolore eu fugiat nulla pariatur. Excepteur sint occaecat cupidatat non proident.</p>
  <div class="solution-video" role="img" aria-label="Video still of a panda climbing a tree">
    <svg class="play-button" viewBox="0 0 54 54"><circle cx="27" cy="27" r="25" fill="rgba(0,0,0,0.15)" stroke="#fff" stroke-width="1.5"/><path d="M22 18 L36 27 L22 36 Z" fill="#fff"/></svg>
  </div>

  <div class="photo photo--panda-cub feature-photo feature-1-photo" role="img" aria-label="Panda cub resting on a branch"></div>
  <h3 class="section-heading section-heading--warm feature-1-heading">PERSPICIATIS UNDE OMNIS</h3>
  <p class="body-copy feature-copy feature-1-copy">Lorem ipsum dolor sit amet, consectetur adipiscing elit, sed do eiusmod tempor incididunt ut labore et dolore magna aliqua. Ut enim ad minim veniam. Duis aute irure dolor in reprehenderit in voluptate velit esse cillum dolore eu fugiat nulla pariatur. Excepteur sint occaecat cupidatat non proident.</p>

  <h3 class="section-heading feature-2-heading">PERSPICIATIS UNDE OMNIS</h3>
  <p class="body-copy feature-copy feature-2-copy">Lorem ipsum dolor sit amet, consectetur adipiscing elit, sed do eiusmod tempor incididunt ut labore et dolore magna aliqua. Ut enim ad minim veniam. Duis aute irure dolor in reprehenderit in voluptate velit esse cillum dolore eu fugiat nulla pariatur. Excepteur sint occaecat cupidatat non proident.</p>
  <div class="photo photo--panda-bamboo feature-photo feature-2-photo" role="img" aria-label="Panda eating bamboo"></div>

  <div class="photo photo--panda-tree feature-photo feature-3-photo" role="img" aria-label="Panda among bamboo stalks"></div>
  <h3 class="section-heading section-heading--warm feature-3-heading">PERSPICIATIS UNDE OMNIS</h3>
  <p class="body-copy feature-copy feature-3-copy">Lorem ipsum dolor sit amet, consectetur adipiscing elit, sed do eiusmod tempor incididunt ut labore et dolore magna aliqua. Ut enim ad minim veniam. Duis aute irure dolor in reprehenderit in voluptate velit esse cillum dolore eu fugiat nulla pariatur. Excepteur sint occaecat cupidatat non proident.</p>

  <section class="closing-band">
    <p class="closing-line">Donate today &amp; help us reach our $1M goal to<br>Lorem Ipsum is simply dummy text of the</p>
    <div class="btn btn--dark btn--closing">Donate Now</div>
  </section>

  <div class="scrim"></div>

  <section class="checkout-modal" aria-label="Donation checkout">
    <div class="modal-header">
      <span class="modal-title">Your Donation Will Make A Difference</span>
      <svg class="modal-close" viewBox="0 0 9 9"><rect width="9" height="9" rx="1" fill="#d6d6d6"/><path d="M2.5 2.5 L6.5 6.5 M6.5 2.5 L2.5 6.5" stroke="#fff" stroke-width="1"/></svg>
    </div>

    <span class="modal-label amount-label">THE AMOUNT:</span>
    <div class="amount-box"><span class="amount-currency">$</span><span class="amount-value">100</span></div>
    <span class="modal-label amount-note">DONATIONS IN USD</span>
    <span class="modal-label donating-label">DONATING TO:</span>
    <div class="charity-logo">LOGO<br>HERE</div>
    <div class="monthly"><span class="check-box"></span><span class="modal-label">Contribute Each Month</span></div>

    <span class="modal-label details-label">YOUR DETAILS:</span>
    <div class="field field--name">First &amp; Last Name<span class="field-social"></span></div>
    <div class="field field--email">Email</div>
    <div class="field field--billing">Billing Address</div>
    <div class="field field--zip">Zip Code</div>
    <div class="field field--card">Credit Card Number</div>
    <div class="field field--month">Month</div>
    <div class="field field--year">Year</div>
    <div class="field field--cvv">CVV</div>
    <div class="field field--message">Add message</div>

    <div class="modal-rule"></div>
    <div class="robot-check">
      <span class="check-box"></span>
      <span class="robot-text">I am not a robot</span>
      <span class="robot-badge"></span>
      <span class="robot-legal">Privacy - Terms</span>
    </div>
    <div class="btn btn--submit">Make Your Donation</div>

    <p class="included-copy">INCLUDED 3 NIGHTS VACATION CERTIFICATE FOR LAS VEGAS!</p>
    <div class="certificate-card" role="img" aria-label="Vacation certificate card showing Las Vegas at night"></div>
    <div class="brought-by brought-by--modal">
      <div class="brought-label">Brought To You By:</div>
      <div class="partner-mark"><span class="partner-dot"></span><span class="partner-name">Willowmere Perks</span></div>
    </div>
  </section>
</main>

</body>
</html>
```